St. Paddy’s Day Invitation

Invitation to text to people:
6th Annual St. Paddy’s Day Party
Where: The Halvorsen’s
When: Saturday, March 25
Acoustic session by Tavin Ashcombe from Mr. Paperlanterns
Fundraiser for Otis Wembley ‘Steady Compass’ Fund

Target Market(s)

Adults only, all friends from our town, Moorestown, NJ

Colors
00AB8E
00BBA5
67D7C9
C6EFE9
E9F9F6
59FF00
82FF00
B8FF75
E3FFCB
F4FFEA

```html
<!DOCTYPE html>
<html lang="en">
<head>
<meta charset="utf-8">
<title>6th Annual St. Paddy’s Day Party</title>
<link href="https://fonts.googleapis.com/css2?family=Alfa+Slab+One&family=Barlow+Condensed:wght@500;600;700&display=swap" rel="stylesheet">
<style>
  :root {
    --ink-dark: #141414;
    --shadow-green: #0f2a17;
    --deep-green: #1d5a32;
    --field-green: #2a6e3e;
    --paper: #f4f4ef;
    --navy: #1b2135;
    --mint-wash: #E9F9F6;
  }
  html, body {
    margin: 0;
    padding: 0;
    width: 849px;
    height: 1200px;
    overflow: hidden;
    background: var(--ink-dark);
  }
  .invite {
    position: relative;
    width: 849px;
    height: 1200px;
    overflow: hidden;
    background:
      radial-gradient(ellipse 90% 70% at 30% 20%, #5a5d5a 0%, rgba(40,45,42,0.6) 45%, rgba(0,0,0,0) 75%),
      linear-gradient(160deg, #2e302f 0%, var(--shadow-green) 45%, var(--deep-green) 80%, var(--field-green) 100%);
    font-family: "Barlow Condensed", "Arial Narrow", sans-serif;
    color: var(--paper);
  }
  .performer-photo {
    position: absolute;
    left: 0;
    top: 0;
    width: 360px;
    height: 1200px;
    background:
      radial-gradient(ellipse 70% 20% at 35% 12%, #8d8f8c 0%, rgba(141,143,140,0) 70%),
      linear-gradient(180deg, #3c3e3c 0%, #1a1c1b 45%, #0d120e 100%);
    opacity: 0.85;
    -webkit-mask-image: linear-gradient(90deg, #000 70%, transparent 100%);
            mask-image: linear-gradient(90deg, #000 70%, transparent 100%);
  }
  .fund-mark {
    position: absolute;
    top: 86px;
    right: 40px;
    display: flex;
    align-items: center;
    gap: 12px;
  }
  .fund-mark__dot {
    width: 22px;
    height: 22px;
    border-radius: 50%;
    background: var(--paper);
  }
  .fund-mark__name {
    font-weight: 700;
    font-size: 34px;
    line-height: 1;
    text-transform: uppercase;
    color: var(--paper);
    letter-spacing: 0.5px;
  }
  .headline {
    position: absolute;
    right: 40px;
    top: 312px;
    margin: 0;
    text-align: right;
    font-family: "Alfa Slab One", "Rockwell", serif;
    font-weight: 400;
    font-size: 60px;
    line-height: 68px;
    letter-spacing: 1px;
    text-transform: uppercase;
    color: var(--paper);
  }
  .details {
    position: absolute;
    right: 40px;
    top: 652px;
    margin: 0;
    text-align: right;
    font-weight: 500;
    font-size: 46px;
    line-height: 78px;
    color: var(--paper);
  }
  .lineup {
    position: absolute;
    right: 40px;
    top: 862px;
    display: flex;
    flex-direction: column;
    align-items: flex-end;
    text-align: right;
  }
  .lineup__intro {
    font-weight: 500;
    font-size: 33px;
    line-height: 40px;
    margin-right: 6px;
  }
  .lineup__artist {
    margin-top: 10px;
    padding: 4px 16px 2px;
    background: var(--paper);
    color: var(--navy);
    font-weight: 700;
    font-size: 54px;
    line-height: 64px;
    text-transform: uppercase;
    letter-spacing: 0.5px;
  }
  .lineup__band {
    margin-top: 10px;
    font-weight: 500;
    font-size: 34px;
    line-height: 42px;
    margin-right: 6px;
  }
  .lineup__cause {
    margin-top: 4px;
    font-weight: 600;
    font-size: 20px;
    line-height: 26px;
  }
</style>
</head>
<body>
  <main class="invite">
    <div class="performer-photo" role="img" aria-label="Black and white photo of a singer in glasses performing into a handheld microphone"></div>

    <div class="fund-mark">
      <span class="fund-mark__dot"></span>
      <span class="fund-mark__name">Steady Compass Fund</span>
    </div>

    <h1 class="headline">6th Annual<br>St. Paddy’s<br>Day Party</h1>

    <p class="details">at The Halvorsen’s<br>on Saturday, March 25</p>

    <section class="lineup">
      <span class="lineup__intro">Acoustic session by</span>
      <span class="lineup__artist">Tavin Ashcombe</span>
      <span class="lineup__band">from Mr. Paperlanterns</span>
      <span class="lineup__cause">(Fundraiser for Otis Wembley ‘Steady Compass’ Fund)</span>
    </section>
  </main>
</body>
</html>
```